Business Card Design for Property Development Company Director

I am looking for a professional and unforgettable business card design for our Director of our Property Development Company.
Please see attached .pptx file to find out what information to include. You don't have to follow the exact format shown in the file - I am interested to see your creative flair using the information provided.

```html
<!DOCTYPE html>
<html lang="en">
<head>
<meta charset="utf-8">
<title>Norwell Property Group – Business Card</title>
<link href="https://fonts.googleapis.com/css2?family=Montserrat:wght@500;600;700&family=Open+Sans:wght@400;600&display=swap" rel="stylesheet">
<style>
  :root {
    --backdrop: #2a2a2c;
    --brand-blue: #0e55a8;
    --ink: #2e2e30;
    --ink-muted: #555659;
    --rule: #6b6b6e;
    --paper: #ffffff;
    --on-blue: #ffffff;
    --mark-dark: #1c1c1e;
  }
  * { margin: 0; padding: 0; box-sizing: border-box; }
  html, body {
    width: 1200px; height: 895px; overflow: hidden;
    background: var(--backdrop);
  }
  .stage {
    width: 1200px; height: 895px;
    display: flex; flex-direction: column; align-items: center; justify-content: center;
    gap: 32px;
  }
  .card {
    width: 700px; height: 400px; position: relative; overflow: hidden;
    box-shadow: 0 10px 28px rgba(0,0,0,.45);
  }

  /* Front */
  .card--front { background: var(--brand-blue); color: var(--on-blue); }
  .front__tagline {
    position: absolute; top: 44px; left: 0; right: 0; text-align: center;
    font: 600 22px/1.3 "Open Sans", sans-serif; letter-spacing: .3px;
  }
  .front__map {
    position: absolute; left: 150px; top: 130px; width: 420px; height: 170px;
    background: radial-gradient(ellipse at center, rgba(255,255,255,.14), rgba(255,255,255,0) 70%);
  }
  .front__brand {
    position: absolute; top: 184px; left: 0; right: 0;
    display: flex; align-items: center; justify-content: center; gap: 16px;
  }
  .front__brand .brand__square { width: 42px; height: 42px; background: var(--mark-dark); flex: none; }
  .front__brand .brand__name {
    font: 700 34px/1 "Montserrat", sans-serif; letter-spacing: .5px; color: var(--mark-dark);
    white-space: nowrap;
  }
  .front__offer {
    position: absolute; bottom: 40px; left: 0; right: 0; text-align: center;
    font: 500 15px/1 "Open Sans", sans-serif; letter-spacing: .8px; text-transform: uppercase;
  }

  /* Back */
  .card--back { background: var(--paper); color: var(--ink); }
  .back__brand {
    position: absolute; top: 58px; left: 48px;
    display: flex; align-items: center; gap: 14px;
  }
  .back__brand .brand__square { width: 40px; height: 40px; background: var(--brand-blue); flex: none; }
  .back__brand .brand__name {
    font: 700 30px/1 "Montserrat", sans-serif; color: var(--brand-blue); letter-spacing: .5px;
    white-space: nowrap;
  }
  .holder {
    position: absolute; top: 150px; left: 48px; right: 48px;
  }
  .holder__line {
    display: flex; align-items: flex-end; gap: 0;
  }
  .holder__rule { flex: 1; height: 1px; background: var(--rule); margin-bottom: 2px; }
  .holder__name {
    font: 700 27px/1 "Montserrat", sans-serif; color: var(--brand-blue);
    letter-spacing: -.5px; text-transform: uppercase; white-space: nowrap;
  }
  .holder__role {
    margin-top: 8px; text-align: right;
    font: 400 17px/1 "Open Sans", sans-serif; color: var(--ink);
  }
  .holder__licence {
    position: absolute; top: 238px; right: 48px;
    font: 400 14px/1 "Open Sans", sans-serif; color: var(--ink-muted);
  }
  .contact {
    position: absolute; left: 48px; bottom: 40px; list-style: none;
  }
  .contact__item {
    display: flex; align-items: center; gap: 12px;
    font: 400 17px/1 "Open Sans", sans-serif; color: var(--ink); margin-bottom: 10px;
  }
  .contact__item:last-child { margin-bottom: 0; }
  .contact__icon { width: 16px; height: 16px; flex: none; }
</style>
</head>
<body>
<main class="stage">
  <section class="card card--front" aria-label="Card front">
    <p class="front__tagline">Property Development<br>&amp; Site Acquisition Specialists</p>
    <div class="front__map" role="img" aria-label="Faint dotted world map behind the company name"></div>
    <div class="front__brand">
      <span class="brand__square"></span>
      <span class="brand__name">NORWELL PROPERTY GROUP</span>
    </div>
    <p class="front__offer">Ask me about our investment &amp; partnership opportunities</p>
  </section>

  <section class="card card--back" aria-label="Card back">
    <div class="back__brand">
      <span class="brand__square"></span>
      <span class="brand__name">NORWELL PROPERTY GROUP</span>
    </div>

    <div class="holder">
      <div class="holder__line">
        <span class="holder__rule"></span>
        <p class="holder__name">Daniel Marsh</p>
      </div>
      <p class="holder__role">Director</p>
    </div>
    <p class="holder__licence">Real Estate Lic: 1234567 &amp; 1234568</p>

    <ul class="contact">
      <li class="contact__item">
        <svg class="contact__icon" viewBox="0 0 24 24" fill="var(--brand-blue)"><path d="M6.6 10.8a15.1 15.1 0 0 0 6.6 6.6l2.2-2.2a1 1 0 0 1 1-.25 11.4 11.4 0 0 0 3.6.57 1 1 0 0 1 1 1V20a1 1 0 0 1-1 1A17 17 0 0 1 3 4a1 1 0 0 1 1-1h3.5a1 1 0 0 1 1 1c0 1.25.2 2.45.57 3.57a1 1 0 0 1-.25 1z"/></svg>
        0400 123 456
      </li>
      <li class="contact__item">
        <svg class="contact__icon" viewBox="0 0 24 24" fill="none" stroke="var(--brand-blue)" stroke-width="2"><rect x="3" y="5" width="18" height="14"/><path d="M3 6l9 7 9-7"/></svg>
        daniel@norwell.com.au
      </li>
      <li class="contact__item">
        <svg class="contact__icon" viewBox="0 0 24 24" fill="none" stroke="var(--brand-blue)" stroke-width="2"><circle cx="12" cy="12" r="9"/><path d="M3 12h18M12 3c3 3.5 3 14.5 0 18M12 3c-3 3.5-3 14.5 0 18"/></svg>
        www.norwell.com.au
      </li>
    </ul>
  </section>
</main>
</body>
</html>
```